professional coaching community needs new look for website

We require a website design that attracts professionals. We run a large, global professional coaching community (e.g. executive, business, personal coaches NOT sports coaches). Our members are committed to their professional and personal development and they enjoy building relationships with other coaches across the world. We also champion the success of coaches and the coaching industry by providing business support resources to our members. We do not mind which colours you use, but whatever the combination, the combinations must be professional and refined. It would be good to have some of the familiarity of the old site colours, with some new, more professional element. We have a number of requirements for the homepage and members design, and this is attached.

Reason: I am extending the deadline for this design, in order to give feedback and see how current designs can be tweaked.

Target Market(s)

Here are some ideas for images, which gives and idea of the target market also:

Ideas for website images:

1. http://www.pixelvarno.com/stock-photo-48213077-business-success.php?st=4b2a918 (I like the people in this one – they seem very dynamic and a good mix of women and men)
2. http://www.pixelvarno.com/stock-photo-51729406-business-communications.php?st=4b2a918 (I like all of the speech bubbles in this one, that’s what the MentraLoop community does – pairs up in two’s or small groups and engages in professional talking)
3. http://www.pixelvarno.com/stock-photo-37086152-global-business-working.php?st=4b2a918 (I like the combination of the world and the people talking in different groups)
4. http://www.pixelvarno.com/stock-photo-44861039-global-business-people.php?st=e512604 (I like the world in this one – would be good to see combination of world and #1 dynamic people, which is the MentraLoop community)

Industry/Entity Type

Building

Requirements
Must have
• See attached uploaded files including homepage design, member dashboard design, and example profile (profiles need to be included him banner design). Note that any text must not be build into graphic. It needs to be able to be edited via html.

```html
<!DOCTYPE html>
<html lang="en">
<head>
<meta charset="utf-8">
<title>MentraLoop – Reciprocal peer coaching, mentoring and supervision</title>
<link href="https://fonts.googleapis.com/css2?family=Ubuntu:ital,wght@0,300;0,400;0,500;1,400&display=swap" rel="stylesheet">
<style>
:root{
  --green-light:#8cc98a;
  --green-mid:#6aad68;
  --green-band:#5c9f5b;
  --green-text:#4e9a4c;
  --blue:#0f5089;
  --blue-dark:#22497a;
  --orange:#f08a1c;
  --orange-dark:#e0730a;
  --ink:#444;
  --ink-soft:#555;
  --line:#e3e3e3;
  --footer:#3d3d3d;
}
*{box-sizing:border-box;margin:0;padding:0}
html,body{width:1006px;height:1200px;overflow:hidden;background:#fff}
body{font-family:"Ubuntu",sans-serif;color:var(--ink)}
.page{position:relative;width:1200px;height:1431px;transform:scale(0.838333);transform-origin:0 0;background:#fff}
.abs{position:absolute}

/* header */
.header{left:0;top:0;width:1200px;height:141px;background:linear-gradient(#90cc8e,#86c584)}
.brand{left:120px;top:48px}
.brand-name{font-size:27px;font-weight:500;color:#fff;letter-spacing:.5px;display:flex;align-items:center;gap:8px}
.brand-name .dot{width:12px;height:12px;border-radius:50%;background:var(--blue-dark)}
.brand-tag{font-size:12px;font-style:italic;color:var(--blue-dark);margin:6px 0 0 56px;line-height:15px}
.lang{left:953px;top:17px;width:128px;height:28px;background:#fff;border:1px solid #d5d5d5;border-radius:2px;font-size:11px;color:#666;display:flex;align-items:center;padding-left:8px;gap:8px}
.lang .flag{width:26px;height:15px;background:#2d3f8f}
.lang .caret{margin-left:auto;margin-right:8px;width:0;height:0;border-left:6px solid transparent;border-right:6px solid transparent;border-top:5px solid #aaa}
.nav{left:413px;top:82px;display:flex;height:34px}
.nav a{color:#fff;text-decoration:none;font-size:14px;line-height:34px;padding:0 12px}
.nav a.active{background:var(--blue-dark);padding:0 13px}

.band{left:0;top:141px;width:1200px;height:69px;background:var(--green-band)}
.band h1{position:absolute;left:120px;top:14px;font-weight:400;font-size:29px;color:#fff}
.btn-orange{background:linear-gradient(#f5982e,var(--orange-dark));color:#fff;border-radius:3px;font-weight:500;text-align:center;box-shadow:0 1px 2px rgba(0,0,0,.25)}
.band .btn-orange{position:absolute;left:886px;top:15px;width:153px;height:40px;line-height:40px;font-size:17px}

.backdrop{left:0;top:210px;width:1200px;height:86px;background:linear-gradient(#e4e4e4,#fff)}

/* why card */
.why{left:120px;top:221px;width:710px;height:243px;background:#fff;border:1px solid #e0e0e0;border-radius:2px;padding:18px 18px}
.why h2{font-weight:400;font-size:25px;color:var(--blue-dark);margin-bottom:12px}
.ticks{list-style:none}
.ticks li{position:relative;padding-left:24px;font-size:13px;line-height:28px;color:var(--ink)}
.ticks svg{position:absolute;left:0;top:9px}
.more{display:inline-block;margin-top:10px;font-size:13px;color:var(--green-text);text-decoration:underline}

/* hero */
.hero{left:120px;top:479px;width:710px;height:330px;background:#e0e0e0;padding:5px}
.hero-photo{width:700px;height:320px;background:linear-gradient(#4a7aa8 0%,#8ab0c8 35%,#f2d08a 62%,#e59a3a 75%,#3a3228 100%);position:relative}
.hero-caption{position:absolute;left:0;bottom:0;width:700px;height:90px;background:rgba(30,30,30,.72)}
.hero-caption p{position:absolute;left:18px;top:16px;color:#fff;font-size:26px;line-height:27px;width:520px}
.hero-caption .btn-orange{position:absolute;left:536px;top:25px;width:155px;height:38px;line-height:38px;font-size:17px}

/* welcome */
.welcome{left:120px;top:826px;width:680px}
.welcome h2{font-weight:400;font-size:24px;color:var(--blue-dark);padding-left:2px}
.welcome .rule{width:387px;height:4px;background:#e4e4e4;margin:10px 0 20px}
.welcome p{font-size:13.4px;line-height:23px;color:var(--ink-soft);margin-bottom:9px}

/* sidebar */
.login{left:840px;top:221px;width:240px;height:221px;background:var(--green-mid);padding:13px 14px}
.side-title{font-size:18px;color:#fff;font-weight:400;letter-spacing:.3px}
.field{height:28px;background:#fff;border:1px solid #d6d6d6;border-radius:2px;font-size:10.5px;color:#777;padding-left:12px;line-height:26px;margin-top:11px}
.row{display:flex;align-items:center;gap:7px;font-size:13px;color:#fff}
.check{width:14px;height:14px;background:#f3f3f3;border:1px solid #ccc;flex:none}
.btn-blue{margin-left:auto;background:var(--blue);color:#fff;font-size:13px;padding:0 13px;height:27px;line-height:27px}
.login .links{font-size:12.5px;color:#fff;line-height:23px;margin-top:14px;padding-left:3px}

.signup{left:840px;top:451px;width:240px;height:452px;background:var(--blue);padding:13px 14px}
.signup .ticks li{color:#fff;font-size:13px;line-height:18px;padding:5px 40px 5px 27px}
.signup .ticks svg{top:9px}
.signup .ticks{margin-top:6px;margin-bottom:8px}
.terms{display:flex;gap:9px;font-size:13px;color:#fff;line-height:20px;margin-top:11px}
.terms .check{margin-top:4px}
.btn-green{position:absolute;right:15px;bottom:15px;background:#6aad68;color:#fff;font-size:13px;width:116px;height:27px;line-height:27px;text-align:center}

.focus{left:840px;top:913px;width:240px;height:154px;background:linear-gradient(#5784b8,#9fbfdc 55%,#cfd9dd 72%,#2f5f7e 100%);padding:6px 11px;color:#fff}
.focus h3{font-weight:400;font-size:22px}
.focus li{list-style:none;font-size:10px;line-height:16px}

/* lower */
.divider{left:120px;top:1090px;width:960px;height:1px;background:var(--line)}
.events{left:120px;top:1107px;width:455px}
.sec-title{font-size:23px;font-weight:400;color:var(--blue-dark);padding-left:1px}
.sec-rule{height:4px;background:#e4e4e4;margin:10px 0 20px}
.arrows{position:absolute;right:5px;top:6px;display:flex;gap:14px}
.events h4{font-size:17px;font-weight:400;color:var(--green-text);margin-bottom:6px}
.events p{font-size:12.3px;line-height:23px;color:var(--ink-soft);width:425px}
.events p em{color:var(--blue-dark)}
.vline{left:592px;top:1112px;width:1px;height:188px;background:var(--line)}
.supporters{left:609px;top:1107px;width:471px}
.logos{display:grid;grid-template-columns:repeat(3,150px);gap:14px 10px}
.logo{height:57px;border:1px solid #e0e0e0;background:#f7f7f7;display:flex;align-items:center;justify-content:center;gap:7px;font-size:17px;color:#555}
.logo .mk{width:14px;height:14px;border-radius:50%;background:#999}

/* footer */
.footer{left:0;top:1317px;width:1200px;height:114px;background:var(--footer)}
.copy{position:absolute;left:120px;top:35px;font-size:12px;color:#ddd;line-height:23px}
.copy span{color:#7cc07a}
.connect{position:absolute;right:120px;top:20px;text-align:right;font-size:13px;color:#fff}
.socials{display:flex;gap:10px;margin-top:12px;justify-content:flex-end}
.socials i{width:30px;height:30px;border-radius:3px;background:#5e86b8;display:block}
.socials i:nth-child(4){background:#c7332c}
</style>
</head>
<body>
<div class="page">

  <header class="header abs">
    <div class="brand abs">
      <div class="brand-name"><span class="dot"></span>MentraLoop</div>
      <div class="brand-tag">Reciprocal peer coaching,<br>&nbsp;&nbsp;&nbsp;&nbsp;mentoring and supervision</div>
    </div>
    <div class="lang abs"><span class="flag" role="img" aria-label="English flag"></span>ENGLISH<span class="caret"></span></div>
    <nav class="nav abs">
      <a class="active">HOME</a><a>COACHING</a><a>MENTORING</a><a>SUPERVISION</a><a>RESOURCES</a><a>JOIN US</a><a>CONTACT US</a>
    </nav>
  </header>

  <section class="band abs">
    <h1>Join the Most Dynamic Coaching Community in the World</h1>
    <div class="btn-orange">QUICK SIGNUP</div>
  </section>
  <div class="backdrop abs"></div>

  <section class="why abs">
    <h2>Why Choose MentraLoop?</h2>
    <ul class="ticks">
      <li><svg width="12" height="11" viewBox="0 0 12 11"><path d="M1 6l3.5 3.5L11 1" fill="none" stroke="#22497a" stroke-width="2.2"/></svg>Demonstrate integrity (coaching), competency (mentoring) and professionlism (supervision)</li>
      <li><svg width="12" height="11" viewBox="0 0 12 11"><path d="M1 6l3.5 3.5L11 1" fill="none" stroke="#22497a" stroke-width="2.2"/></svg>Be part of one of the most active coaching communities in the world</li>
      <li><svg width="12" height="11" viewBox="0 0 12 11"><path d="M1 6l3.5 3.5L11 1" fill="none" stroke="#22497a" stroke-width="2.2"/></svg>Be at your edge personally and professionally</li>
      <li><svg width="12" height="11" viewBox="0 0 12 11"><path d="M1 6l3.5 3.5L11 1" fill="none" stroke="#22497a" stroke-width="2.2"/></svg>Remove the isolation normally attached to working for yourself</li>
      <li><svg width="12" height="11" viewBox="0 0 12 11"><path d="M1 6l3.5 3.5L11 1" fill="none" stroke="#22497a" stroke-width="2.2"/></svg>All the known benefits of coaching, mentoring and supervision</li>
    </ul>
    <a class="more">READ MORE &gt;&gt;</a>
  </section>

  <section class="hero abs">
    <div class="hero-photo" role="img" aria-label="Silhouettes of a cheering group of business people against a sunset sky">
      <div class="hero-caption">
        <p>Personal &amp; Professional Development for Coaches</p>
        <div class="btn-orange">GET STARTED</div>
      </div>
    </div>
  </section>

  <section class="welcome abs">
    <h2>Welcome to Our MainPage</h2>
    <div class="rule"></div>
    <p>MentraLoop is an international community of coaches who engage in reciprocal coaching, mentoring and supervision for their own personal and professional development.</p>
    <p>By giving coaching and mentoring, MentraLoop coaches receive coaching and mentoring, and by participating in supervision, MentraLoop coaches give and receive through collaborative learning.</p>
    <p>Therefore, as a MentraLoop coach, you pay for your coaching, mentoring and supervision by giving it to another coach. As a result, because you're only paying us to orchestrate the reciprocal process, not for the coaching/ mentoring/supervision itself, 8 sessions can cost much less than you'd normally pay for one session!</p>
  </section>

  <aside class="login abs">
    <div class="side-title">MEMBER LOG IN</div>
    <div class="field">USERNAME</div>
    <div class="field">PASSWORD</div>
    <div class="row" style="margin-top:9px"><span class="check"></span>Keep me logged in<span class="btn-blue">LOG IN</span></div>
    <div class="links">Forgotten login?<br>Not a MentraLoop coach yet?</div>
  </aside>

  <aside class="signup abs">
    <div class="side-title">QUICK SIGN UP</div>
    <ul class="ticks">
      <li><svg width="12" height="11" viewBox="0 0 12 11"><path d="M1 6l3.5 3.5L11 1" fill="none" stroke="#fff" stroke-width="2.2"/></svg>Free to join</li>
      <li><svg width="12" height="11" viewBox="0 0 12 11"><path d="M1 6l3.5 3.5L11 1" fill="none" stroke="#fff" stroke-width="2.2"/></svg>3 issues of Coaching Research in Practice</li>
      <li><svg width="12" height="11" viewBox="0 0 12 11"><path d="M1 6l3.5 3.5L11 1" fill="none" stroke="#fff" stroke-width="2.2"/></svg>Monthly issues of Lessons from the Field</li>
      <li><svg width="12" height="11" viewBox="0 0 12 11"><path d="M1 6l3.5 3.5L11 1" fill="none" stroke="#fff" stroke-width="2.2"/></svg>Access to our community</li>
      <li><svg width="12" height="11" viewBox="0 0 12 11"><path d="M1 6l3.5 3.5L11 1" fill="none" stroke="#fff" stroke-width="2.2"/></svg>Online profile</li>
    </ul>
    <div class="field">FIRST NAME</div>
    <div class="field" style="margin-top:12px">LAST NAME</div>
    <div class="field" style="margin-top:12px">EMAIL ADDRESS</div>
    <div class="terms"><span class="check"></span>I have read the MentraLoop terms and conditions.</div>
    <div class="btn-green">SIGN UP NOW</div>
  </aside>

  <aside class="focus abs" role="img" aria-label="Business team meeting at a table on a beach">
    <h3>Focusing on Change</h3>
    <ul><li>• Changing Behavior</li><li>• Driving Results</li><li>• Creating Sustainable Growth</li></ul>
  </aside>

  <div class="divider abs"></div>

  <section class="events abs">
    <div class="sec-title">Upcoming Events</div>
    <div class="arrows">
      <svg width="10" height="18" viewBox="0 0 10 18"><path d="M8 2L2 9l6 7" fill="none" stroke="#555" stroke-width="2.4"/></svg>
      <svg width="10" height="18" viewBox="0 0 10 18"><path d="M2 2l6 7-6 7" fill="none" stroke="#555" stroke-width="2.4"/></svg>
    </div>
    <div class="sec-rule"></div>
    <h4>New Rounds Starting Soon</h4>
    <p>There is at least one round of coaching, mentoring or supervision starting every month. You can also plan ahead and register for rounds months in advance. ... <em>Read More</em></p>
  </section>
  <div class="vline abs"></div>

  <section class="supporters abs">
    <div class="sec-title">Thanks to our Supporters</div>
    <div class="sec-rule"></div>
    <div class="logos">
      <div class="logo"><span class="mk"></span>Quillrex.co</div>
      <div class="logo">Aldermoor.Co</div>
      <div class="logo"><span class="mk"></span>Zyntera</div>
      <div class="logo"><span class="mk"></span>Korvaline</div>
      <div class="logo"><span class="mk"></span>Pellworth</div>
      <div class="logo"><span class="mk"></span>Brannoch's</div>
    </div>
  </section>

  <footer class="footer abs">
    <div class="copy">Copyright © 2009-2013 <span>MentraLoop Pty Ltd.</span><br>All Right Reserved</div>
    <div class="connect">Connect with our Community
      <div class="socials"><i aria-label="Social link"></i><i aria-label="Social link"></i><i aria-label="Social link"></i><i aria-label="Video channel"></i></div>
    </div>
  </footer>

</div>
</body>
</html>
```